IT Logo and business card design

Would like to create a business card and logo for a new company out of Orlando, FL named Torvane IT services. We will be providing IT related services to both residential and business clients. I would love if the front of the card has a logo, Tagline and contact details.. Real clean
I like the blue color wheel when referencing technology but open to your creativity.

Target Market(s)

Small/Medium sized businesses.

Industry/Entity Type

Information Technology

Contact Information for Business Card

Company Name:Torvane IT services
Oscar Torvane
Owner
321-555-0187
www.TorvaneITservices.com
OscarTorvane@TorvaneITservices.com

Tagline: IT servicing today saves money tomorrow.

The back would have the following (possibly centered but trust your thoughts)

Free onsite evaluation
Free same day estimate
Quality service
To book online visit www.TorvaneITservices.com
or call 321-555-0187

Last line:
We look forward to working with you!

Thank you

Font styles to use
Serif
Sans Serif

Colors
85acd3
3176b5
0555a3
ec1f27

Requirements
Must have
• Company Name:Torvane IT services (would be nice if the IT in the company name would stand out)
• Oscar Torvane (Larger font/Bolded)
• Tagline: IT servicing today saves money tomorrow. (on Front)
• (everything below on back)
• Free onsite evaluation
• Free same day estimate
• Quality service
• To book online visit www.TorvaneITservices.com
• or call 321-555-0187
• Last line:
• We look forward to working with you!
Nice to have
• I would like the logo to play off the name Torvane and incorporate technology.
• or have the Logo embedded with the IT of the company name.

```html
<!DOCTYPE html>
<html lang="en">
<head>
<meta charset="utf-8">
<title>Torvane IT Services – Identity</title>
<link rel="stylesheet" href="https://fonts.googleapis.com/css2?family=Michroma&family=Questrial&family=Roboto+Slab:wght@700&display=swap">
<style>
  :root {
    --gray: #5d5f61;
    --gray-soft: #8a8c8e;
    --blue-light: #6aaadc;
    --blue: #2f74ad;
    --navy: #0d4a78;
    --paper: #ffffff;
    --table: #e6e9ec;
  }
  * { box-sizing: border-box; margin: 0; padding: 0; }
  html, body { width: 1200px; height: 1000px; overflow: hidden; }
  body { background: var(--table); font-family: "Questrial", sans-serif; color: var(--gray); }

  .brand-area {
    height: 395px; background: var(--paper);
    display: flex; flex-direction: column; align-items: center; justify-content: center; gap: 26px;
  }
  .brand-mark { display: flex; align-items: center; gap: 20px; }
  .brand-square { width: 40px; height: 40px; background: var(--blue-light); }
  .brand-name { font-family: "Michroma", sans-serif; font-size: 46px; color: var(--navy); letter-spacing: 2px; }
  .brand-tagline {
    font-family: "Roboto Slab", serif; font-weight: 700; font-size: 19px;
    letter-spacing: 3.5px; color: var(--blue-light); text-transform: uppercase;
  }

  .cards { display: flex; justify-content: center; gap: 60px; padding-top: 150px; }
  .card {
    position: relative; width: 520px; height: 298px; background: var(--paper);
    overflow: hidden; box-shadow: 0 10px 30px rgba(0,0,0,.18);
  }
  .card-art { position: absolute; inset: 0; }

  /* front */
  .card-front .side-band {
    position: absolute; left: 0; top: 0; bottom: 0; width: 24px; background: var(--blue);
    display: flex; flex-direction: column; justify-content: flex-end; align-items: center; gap: 9px; padding-bottom: 18px;
  }
  .card-front .logo { position: absolute; left: 54px; top: 40px; display: flex; align-items: center; gap: 10px; }
  .card-front .logo .brand-square { width: 16px; height: 16px; }
  .card-front .logo .brand-name { font-size: 19px; letter-spacing: 1px; }
  .card-front .tagline {
    position: absolute; left: 54px; top: 74px; font-family: "Roboto Slab", serif; font-weight: 700;
    font-size: 8.5px; letter-spacing: 1.4px; color: var(--blue-light); text-transform: uppercase;
  }
  .person { position: absolute; left: 54px; top: 152px; }
  .person-name { font-size: 22px; font-weight: 700; letter-spacing: 1px; color: var(--gray); text-transform: uppercase; -webkit-text-stroke: .5px var(--gray); }
  .person-name .surname { color: var(--blue); -webkit-text-stroke: .5px var(--blue); }
  .person-role { font-size: 13px; letter-spacing: 1px; color: var(--gray-soft); margin-top: 2px; }
  .contact { position: absolute; left: 54px; bottom: 20px; font-size: 12.5px; line-height: 18px; color: var(--gray); }

  /* back */
  .card-back .content { position: absolute; inset: 0; display: flex; flex-direction: column; align-items: center; text-align: center; padding-top: 58px; }
  .offer { font-size: 25px; line-height: 30px; color: var(--gray); }
  .offer .accent { color: var(--blue-light); }
  .offer-quality { font-size: 25px; color: var(--blue-light); margin-top: 2px; }
  .booking { font-size: 13px; line-height: 18px; color: var(--gray); margin-top: 22px; }
  .closing { font-size: 12.5px; letter-spacing: 1.5px; color: var(--blue); text-transform: uppercase; margin-top: 18px; }
</style>
</head>
<body>
  <header class="brand-area">
    <div class="brand-mark">
      <span class="brand-square"></span>
      <span class="brand-name">TORVANE IT SERVICES</span>
    </div>
    <p class="brand-tagline">IT servicing today saves money tomorrow</p>
  </header>

  <main class="cards">
    <section class="card card-front" aria-label="Business card front">
      <svg class="card-art" viewBox="0 0 520 298" preserveAspectRatio="none" aria-hidden="true">
        <path d="M390 0 C 450 10, 430 110, 520 150 L520 0 Z" fill="var(--blue)"/>
        <path d="M420 0 C 470 20, 460 90, 520 118 L520 0 Z" fill="var(--blue-light)" opacity=".55"/>
      </svg>
      <div class="side-band">
        <svg width="12" height="12" viewBox="0 0 12 12" aria-label="Phone"><rect x="3" y="0.5" width="6" height="11" rx="1" fill="none" stroke="#fff" stroke-width="1.2"/><circle cx="6" cy="9.5" r=".8" fill="#fff"/></svg>
        <svg width="12" height="12" viewBox="0 0 12 12" aria-label="Email"><rect x="0.6" y="2.5" width="10.8" height="7" fill="none" stroke="#fff" stroke-width="1.2"/><path d="M1 3 L6 7 L11 3" fill="none" stroke="#fff" stroke-width="1.2"/></svg>
        <svg width="12" height="12" viewBox="0 0 12 12" aria-label="Website"><circle cx="6" cy="6" r="5.2" fill="none" stroke="#fff" stroke-width="1.1"/><ellipse cx="6" cy="6" rx="2.3" ry="5.2" fill="none" stroke="#fff" stroke-width="1"/><path d="M1 6 H11" stroke="#fff" stroke-width="1"/></svg>
      </div>
      <div class="logo"><span class="brand-square"></span><span class="brand-name">TORVANE IT SERVICES</span></div>
      <p class="tagline">IT servicing today saves money tomorrow</p>
      <div class="person">
        <p class="person-name">Oscar <span class="surname">Torvane</span></p>
        <p class="person-role">OWNER</p>
      </div>
      <address class="contact" style="font-style:normal">
        <div>321 555 0187</div>
        <div>oscartorvane@torvaneitservices.com</div>
        <div>www.torvaneitservices.com</div>
      </address>
    </section>

    <section class="card card-back" aria-label="Business card back">
      <svg class="card-art" viewBox="0 0 520 298" preserveAspectRatio="none" aria-hidden="true">
        <path d="M0 200 C 60 210, 100 300, 200 298 L0 298 Z" fill="var(--blue)"/>
        <path d="M0 232 C 50 240, 80 290, 140 298 L0 298 Z" fill="var(--blue-light)" opacity=".6"/>
        <path d="M400 0 C 450 15, 450 70, 520 90 L520 0 Z" fill="var(--blue)"/>
        <path d="M440 0 C 475 15, 480 50, 520 62 L520 0 Z" fill="var(--blue-light)" opacity=".55"/>
      </svg>
      <div class="content">
        <p class="offer"><span class="accent">Free</span> Onsite Evaluation</p>
        <p class="offer"><span class="accent">Free</span> Same Day Estimate</p>
        <p class="offer-quality">— Quality Service —</p>
        <p class="booking">To book online visit www.torvaneitservices.com or<br>Call 321-555-0187</p>
        <p class="closing">We look forward to working with you!</p>
      </div>
    </section>
  </main>
</body>
</html>
```